Course Graduation Certificate

This project is not for a flyer but instead for the creation of a course graduation certificate. The final certificate needs to include the Marrow Summit Aviation Academy logo and the text stating as follows:
Certifies that ___________________________ has satisfactorily completed the course of _______________________________ on ________________________________
I would also like to include some type of gold seal of completion as well as a place to sign my name and credentials at the bottom of the certificate
I have included the Marrow Summit Aviation Academy logo as well as three other certificate examples for you to work from.
Target Market(s)
Students completing a certification course and receiving a certificate

```html
<!DOCTYPE html>
<html lang="en">
<head>
<meta charset="utf-8">
<title>Certificate of Completion – Marrow Summit Aviation Academy</title>
<link rel="stylesheet" href="https://fonts.googleapis.com/css2?family=Pirata+One&family=Montserrat:wght@400;700&display=swap">
<style>
  :root {
    --paper-light: #fdfcf8;
    --paper-edge: #e9e1cd;
    --frame: #8a8074;
    --ornament: #b3a898;
    --ink: #2b2b2b;
    --rule: #8d8d8d;
    --title: #141414;
    --academy: #1a6fc4;
    --gold-light: #f6dc7a;
    --gold: #d4a72c;
    --gold-dark: #9c7412;
  }
  * { margin: 0; padding: 0; box-sizing: border-box; }
  html, body { width: 1200px; height: 927px; overflow: hidden; background: var(--paper-edge); }
  .certificate {
    position: relative;
    width: 1200px;
    height: 927px;
    background: radial-gradient(ellipse at 50% 45%, var(--paper-light) 0%, #f6f1e4 45%, var(--paper-edge) 100%);
    font-family: "Montserrat", sans-serif;
    color: var(--ink);
  }
  .frame-art { position: absolute; inset: 0; }
  .ornament { fill: var(--ornament); opacity: 0.55; }
  .frame-line { fill: none; stroke: var(--frame); stroke-width: 6; }
  .title-arc text {
    font-family: "Pirata One", cursive;
    font-size: 72px;
    fill: var(--title);
  }
  .statement {
    position: absolute;
    left: 0; width: 1200px;
    text-align: center;
    font-size: 24px;
    font-weight: 400;
    letter-spacing: 0.2px;
  }
  .statement--certifies { top: 305px; }
  .statement--completed { top: 430px; }
  .fill-line { position: absolute; height: 1px; background: var(--rule); }
  .fill-line--name { left: 231px; width: 738px; top: 389px; }
  .fill-line--course { left: 231px; width: 738px; top: 514px; }
  .conferred {
    position: absolute;
    left: 339px; top: 556px;
    font-size: 24px;
  }
  .fill-line--date { left: 510px; width: 338px; top: 578px; }
  .seal { position: absolute; left: 525px; top: 623px; width: 150px; height: 150px; }
  .academy-name {
    position: absolute;
    left: 145px; top: 712px;
    width: 250px;
    font-size: 21px;
    font-weight: 700;
    line-height: 1.2;
    color: var(--academy);
  }
  .signature-line { left: 749px; width: 337px; top: 750px; background: #777; }
  .signatory {
    position: absolute;
    left: 749px; width: 337px; top: 762px;
    text-align: center;
    font-size: 22px;
  }
</style>
</head>
<body>
<main class="certificate">
  <svg class="frame-art" width="1200" height="927" viewBox="0 0 1200 927">
    <g role="img" aria-label="Ornate scrollwork border decoration">
      <rect class="ornament" x="185" y="36" width="830" height="34" rx="8"/>
      <rect class="ornament" x="185" y="857" width="830" height="34" rx="8"/>
      <rect class="ornament" x="38" y="190" width="34" height="548" rx="8"/>
      <rect class="ornament" x="1128" y="190" width="34" height="548" rx="8"/>
      <path class="ornament" d="M20 20 H180 Q120 60 90 110 Q60 150 20 180 Z"/>
      <path class="ornament" d="M1180 20 H1020 Q1080 60 1110 110 Q1140 150 1180 180 Z"/>
      <path class="ornament" d="M20 907 H180 Q120 867 90 817 Q60 777 20 747 Z"/>
      <path class="ornament" d="M1180 907 H1020 Q1080 867 1110 817 Q1140 777 1180 747 Z"/>
    </g>
    <path class="frame-line" d="M82 135 V390 M82 535 V790 M1118 135 V390 M1118 535 V790 M210 82 H540 M660 82 H990 M210 845 H540 M660 845 H990"/>
    <path class="frame-line" d="M82 135 Q82 82 135 82 H210 M1118 135 Q1118 82 1065 82 H990 M82 790 Q82 845 135 845 H210 M1118 790 Q1118 845 1065 845 H990"/>
    <g class="title-arc">
      <path id="titleCurve" d="M275 300 Q600 50 950 305" fill="none"/>
      <text text-anchor="middle"><textPath href="#titleCurve" startOffset="50%">Certificate Of Completion</textPath></text>
    </g>
  </svg>

  <p class="statement statement--certifies">Certifies that</p>
  <div class="fill-line fill-line--name"></div>
  <p class="statement statement--completed">has satisfactorily completed the course of</p>
  <div class="fill-line fill-line--course"></div>
  <p class="conferred">conferred on</p>
  <div class="fill-line fill-line--date"></div>

  <svg class="seal" viewBox="0 0 150 150" role="img" aria-label="Gold seal of completion">
    <defs>
      <radialGradient id="sealGold" cx="40%" cy="35%" r="70%">
        <stop offset="0%" stop-color="var(--gold-light)"/>
        <stop offset="60%" stop-color="var(--gold)"/>
        <stop offset="100%" stop-color="var(--gold-dark)"/>
      </radialGradient>
    </defs>
    <circle cx="75" cy="75" r="74" fill="url(#sealGold)"/>
    <circle cx="75" cy="75" r="60" fill="none" stroke="var(--gold-dark)" stroke-width="2" opacity="0.6"/>
  </svg>

  <p class="academy-name">Marrow Summit Aviation Academy</p>

  <div class="fill-line signature-line"></div>
  <p class="signatory">Authorized Signatory</p>
</main>
</body>
</html>
```